I want a business card that is going to show a creative spark but without limiting me to an industry. Something edgy but that wont go out of date. I want it state My business name Serafina Loire, profession - Professional Makeup Artist contact number and email

My service is to provide makeup services from bridal, fashion, photography, film, TV and so on. It is creative and different so i want that to be reflected.

I would like the card double sided.
Updates

 I would LOVE a background on my card something like this image... i can supply an image to be formed like this

Please use the image uploaded

Can we try using the image provided on one side of the card and then writing and details on the other side

Target Market(s)

I am targeting a wide range of people from Creative directors to the individual eg. bride

Industry/Entity Type

Business

Requirements
Must have
• Name: Delphine Hartwell
contact numbe 0417853120
email address:info@serafinaloire.com
website: www.serafinaloire.com
One of the images attached

professional makeup artist / hair stylist

I want it to show creativity
Nice to have
• logo, Double-sided card
Should not have
• the design should not use tradional style. Or images that are not my own

```html
<!DOCTYPE html>
<html lang="en">
<head>
<meta charset="utf-8">
<title>Serafina Loire – Business Cards</title>
<link rel="stylesheet" href="https://fonts.googleapis.com/css2?family=Cinzel:wght@600&family=Crimson+Text:wght@400;600&display=swap">
<style>
  :root {
    --gold: #f9c800;
    --ink: #0c0c0c;
    --paper: #ffffff;
    --soft-white: #e6e6e6;
    --muted: #bdbdbd;
  }
  * { margin: 0; padding: 0; box-sizing: border-box; }
  html, body {
    width: 1200px;
    height: 900px;
    overflow: hidden;
    background: var(--paper);
  }
  .sheet { position: relative; width: 1200px; height: 900px; }

  .card {
    position: absolute;
    width: 526px;
    height: 301px;
    border-radius: 14px;
    overflow: hidden;
  }
  .card--cover { left: 393px; top: 116px; background: var(--ink); }
  .card--light { left: 55px; top: 468px; background: var(--paper); border: 2px solid var(--ink); }
  .card--dark  { left: 618px; top: 468px; background: var(--ink); }

  .portrait {
    position: absolute;
    left: 0; top: 0;
    width: 232px; height: 301px;
    background:
      linear-gradient(180deg, #5a3220 0%, #7a4a34 22%, #e7cdbf 38%, #d9a88e 62%, #1a1414 80%, var(--ink) 100%);
  }
  .portrait::after {
    content: "";
    position: absolute; inset: 0;
    background: linear-gradient(90deg, transparent 60%, var(--ink) 100%);
  }

  .brand-name {
    position: absolute;
    font-family: "Cinzel", "Times New Roman", serif;
    font-weight: 600;
    color: var(--gold);
    letter-spacing: 1px;
    white-space: nowrap;
    line-height: 1;
  }
  .profession {
    position: absolute;
    font-family: "Crimson Text", Georgia, serif;
    white-space: nowrap;
    line-height: 1;
  }

  .card--cover .brand-name { left: 245px; top: 124px; font-size: 31px; }
  .card--cover .profession { left: 246px; top: 156px; font-size: 17px; color: var(--soft-white); }

  .card--light .brand-name,
  .card--dark .brand-name { left: 26px; top: 34px; font-size: 25px; }
  .card--light .profession { left: 26px; top: 59px; font-size: 13px; color: var(--ink); }
  .card--dark .profession  { left: 26px; top: 59px; font-size: 13px; color: var(--muted); }

  .bar { position: absolute; height: 14px; width: 117px; }
  .bar--left  { left: 0; background: var(--gold); }
  .bar--right { right: 0; }
  .card--light .bar { top: 143px; }
  .card--light .bar--right { background: var(--ink); }
  .card--dark .bar { top: 143px; }
  .card--dark .bar--right { background: var(--paper); }

  .spaced-name {
    position: absolute;
    left: 117px; right: 117px;
    text-align: center;
    font-family: "Crimson Text", Georgia, serif;
    font-size: 15px;
    letter-spacing: 5px;
    top: 139px;
    white-space: nowrap;
  }
  .card--light .spaced-name { color: var(--ink); }
  .card--dark .spaced-name  { color: var(--muted); }

  .contact {
    position: absolute;
    left: 309px;
    top: 205px;
    font-family: "Crimson Text", Georgia, serif;
    font-size: 11.5px;
    line-height: 20px;
    border-collapse: collapse;
  }
  .contact td { padding: 0; white-space: nowrap; }
  .contact .label { width: 34px; }
  .contact .sep { width: 10px; }
  .card--light .contact { color: var(--ink); font-weight: 600; }
  .card--dark .contact  { color: var(--muted); }
</style>
</head>
<body>
<main class="sheet">

  <section class="card card--cover">
    <div class="portrait" role="img" aria-label="Portrait photograph of a model with bold colourful eye makeup, lower face covered by a black veil"></div>
    <h1 class="brand-name">Serafina Loire</h1>
    <p class="profession">Professional Makeup Artist</p>
  </section>

  <section class="card card--light">
    <h2 class="brand-name">Serafina Loire</h2>
    <p class="profession">Professional Makeup Artist</p>
    <span class="bar bar--left"></span>
    <p class="spaced-name">Serafina Loire</p>
    <span class="bar bar--right"></span>
    <table class="contact">
      <tr><td class="label">Tel</td><td class="sep">:</td><td>0417 853 120</td></tr>
      <tr><td class="label">Email</td><td class="sep">:</td><td>serafinaloire@mailbox.com.au</td></tr>
    </table>
  </section>

  <section class="card card--dark">
    <h2 class="brand-name">Serafina Loire</h2>
    <p class="profession">Professional Makeup Artist</p>
    <span class="bar bar--left"></span>
    <p class="spaced-name">Serafina Loire</p>
    <span class="bar bar--right"></span>
    <table class="contact">
      <tr><td class="label">Tel</td><td class="sep">:</td><td>0417 853 120</td></tr>
      <tr><td class="label">Email</td><td class="sep">:</td><td>serafinaloire@mailbox.com.au</td></tr>
    </table>
  </section>

</main>
</body>
</html>
```